Accounting Practice Business Card Design

I have a logo I am happy for you to use in the design of the Business Card.
You can edit and change colours as you please, I am not fixated on it.
I am looking for a modern and clean overall feel for the finished design.

The business is a small accounting practice who thrives on word of mouth referrals and this card will be given to all current and prospect clients.

Industry/Entity Type

Accountant

Contact Information for Business Card

Marcus Elwin
Level 5, 8 Corvale Ridge Road
ASHGROVE RISE VIC 3187
Phone: 9481 3057
Email: melwin@mrfaccountants.com.au
Web: www.mrfaccountants.com.au

Font styles to use
Serif
Sans Serif

Colors
0555a3
3277b5
85acd3
0393ce
33a6d7
85cae6
00a990
33b8a4
9bcb3c

Requirements
Must have
• "The end to your tax problems begin with us"
• "A referral from you is our greatest compliment"
Nice to have
• Modern clean professional

```html
<!DOCTYPE html>
<html lang="en">
<head>
<meta charset="utf-8">
<title>MRF Accountants – Business Card</title>
<link rel="stylesheet" href="https://fonts.googleapis.com/css2?family=Roboto+Condensed:wght@400;700&display=swap">
<style>
  :root {
    --backdrop: #d1d2d4;
    --navy: #13497b;
    --white: #ffffff;
    --green: #2f7a36;
  }
  * { margin: 0; padding: 0; box-sizing: border-box; }
  html, body { width: 1200px; height: 1003px; overflow: hidden; }
  body {
    position: relative;
    background: var(--backdrop);
    font-family: "Roboto Condensed", Arial, sans-serif;
  }
  .card { position: absolute; left: 282px; width: 660px; height: 377px; }
  .card-front { top: 74px; background: var(--navy); color: var(--white); }
  .card-back { top: 553px; background: var(--white); }

  .brand { position: absolute; text-align: center; font-weight: 700; }
  .front-brand { left: 0; right: 0; top: 106px; color: var(--white); }
  .brand-initials { display: block; font-size: 66px; line-height: 62px; letter-spacing: 2px; }
  .brand-word { display: block; font-size: 26px; line-height: 28px; letter-spacing: 1px; }
  .front-brand .brand-word {
    width: 252px; margin: 0 auto; padding-bottom: 4px;
    border-bottom: 2px solid var(--white);
  }
  .front-tagline {
    position: absolute; left: 0; right: 0; top: 236px;
    text-align: center; font-size: 20px;
  }

  .back-brand-panel { position: absolute; left: 0; top: 0; width: 317px; height: 100%; }
  .back-brand { left: 0; right: 0; top: 142px; color: var(--navy); }
  .back-brand .brand-initials { font-size: 58px; line-height: 56px; }
  .back-brand .brand-word { font-size: 22px; line-height: 24px; }
  .back-tagline {
    position: absolute; left: 0; right: 0; top: 245px;
    text-align: center; color: var(--navy); font-size: 14px; line-height: 18px;
  }

  .contact-panel {
    position: absolute; left: 317px; top: 0; width: 343px; height: 100%;
    background: var(--navy); color: var(--white);
  }
  .holder-name {
    position: absolute; right: 38px; top: 70px;
    font-size: 28px; letter-spacing: 3.5px; text-transform: uppercase;
  }
  .name-rule { position: absolute; left: 0; right: 0; top: 120px; height: 2px; background: var(--white); }
  .contact-list { position: absolute; left: 36px; top: 150px; list-style: none; }
  .contact-item { display: flex; align-items: flex-start; height: 43px; font-size: 18px; }
  .contact-icon { width: 32px; height: 32px; margin-right: 23px; flex: none; margin-top: -4px; }
  .contact-text { line-height: 26px; }
</style>
</head>
<body>

<section class="card card-front">
  <div class="brand front-brand">
    <span class="brand-initials">MRF</span>
    <span class="brand-word">ACCOUNTANTS</span>
  </div>
  <p class="front-tagline">The end to your tax problems begin with us</p>
</section>

<section class="card card-back">
  <div class="back-brand-panel">
    <div class="brand back-brand">
      <span class="brand-initials">MRF</span>
      <span class="brand-word">ACCOUNTANTS</span>
    </div>
    <p class="back-tagline">A referral from you is our<br>greatest compliment</p>
  </div>

  <div class="contact-panel">
    <h1 class="holder-name">Marcus Elwin</h1>
    <div class="name-rule"></div>
    <ul class="contact-list">
      <li class="contact-item">
        <svg class="contact-icon" viewBox="0 0 32 32" aria-hidden="true">
          <circle cx="16" cy="16" r="16" fill="#fff"/>
          <path d="M16 7a6 6 0 0 0-6 6c0 4.5 6 11 6 11s6-6.5 6-11a6 6 0 0 0-6-6z" fill="#13497b"/>
          <circle cx="16" cy="13" r="2.3" fill="#fff"/>
        </svg>
        <span class="contact-text">9481 3057</span>
      </li>
      <li class="contact-item">
        <svg class="contact-icon" viewBox="0 0 32 32" aria-hidden="true">
          <circle cx="16" cy="16" r="16" fill="#fff"/>
          <path d="M10.5 8.5l3 -.5 1.8 4-2 1.6c.9 2 2.4 3.6 4.3 4.5l1.6-2 4 1.8-.5 3c-.3 1-1.3 1.6-2.3 1.4C14.5 21.4 10.6 17.5 9.7 11c-.2-1 .5-2.2 .8-2.5z" fill="#13497b"/>
        </svg>
        <span class="contact-text">melwin@mrfaccountants.com.au</span>
      </li>
      <li class="contact-item">
        <svg class="contact-icon" viewBox="0 0 32 32" aria-hidden="true">
          <circle cx="16" cy="16" r="16" fill="#fff"/>
          <circle cx="16" cy="16" r="3.2" fill="none" stroke="#13497b" stroke-width="2.2"/>
          <path d="M19.2 13v4.2c0 1.6 2.8 1.6 2.8-.8a6 6 0 1 0-2.5 4.9" fill="none" stroke="#13497b" stroke-width="2.2"/>
        </svg>
        <span class="contact-text">www.mrfaccountants.com.au</span>
      </li>
      <li class="contact-item">
        <svg class="contact-icon" viewBox="0 0 32 32" aria-hidden="true">
          <circle cx="16" cy="16" r="16" fill="#fff"/>
          <g fill="none" stroke="#13497b" stroke-width="1.8">
            <circle cx="16" cy="16" r="8"/>
            <ellipse cx="16" cy="16" rx="3.5" ry="8"/>
            <path d="M8 16h16M9.3 12h13.4M9.3 20h13.4"/>
          </g>
        </svg>
        <span class="contact-text">Level 5, 8 Corvale Ridge Road<br>&nbsp;ASHGROVE RISE VIC 3187</span>
      </li>
    </ul>
  </div>
</section>

</body>
</html>
```